Classy, Elegant, Simple Business Card Design

Looking to have a classy, simple, and elegant design. Want a top notch designed business card. I really like the look of the new brivo credit card. I also like the design I attached. I am trying to reach 21-29 year old females for booking us for there wedding or event. We offer Disc Jockey Service, Photo Booth Rentals, and Uplighting .

Target Market(s)

21-28 year old females

Contact Information for Business Card

Has to have logo, website, email, and phone number

Font styles to use
Other font styles liked:
• open to font choice, modern, clean
Designer to choose
33a6d7
0791cd
0555a3
ffffff

Requirements
Must have
• Has to have logo, website, email, and phone number
Nice to have
• I really like the design of the new brivo credit card. I also included my logo and some designs I like
Should not have
• clutter or too much info

```html
<!DOCTYPE html>
<html lang="en">
<head>
<meta charset="utf-8">
<title>Echoline Event Group – Business Card</title>
<link rel="stylesheet" href="https://fonts.googleapis.com/css2?family=Open+Sans:wght@400;600;700&display=swap">
<style>
  :root {
    --stage: #3a3a3c;
    --card: #1f2023;
    --blue: #0791cd;
    --blue-deep: #0555a3;
    --blue-light: #33a6d7;
    --white: #ffffff;
    --silver: #b9bcc0;
    --rule: #8a8d91;
  }
  * { margin: 0; padding: 0; box-sizing: border-box; }
  html, body { width: 799px; height: 1200px; overflow: hidden; }
  body {
    background: var(--stage);
    font-family: "Open Sans", Arial, sans-serif;
    position: relative;
  }
  .card {
    position: absolute;
    left: 80px;
    width: 640px;
    height: 366px;
    background: var(--card);
    border-radius: 4px;
    overflow: hidden;
  }
  .card--front { top: 117px; }
  .card--back { top: 717px; }

  /* Front */
  .front-mark {
    position: absolute;
    left: 50%; top: 50%;
    width: 190px; height: 190px;
    transform: translate(-50%, -50%);
    border: 2px solid var(--silver);
    border-radius: 50%;
    display: flex; align-items: center; justify-content: center;
  }
  .brand-name {
    color: var(--blue);
    font-weight: 600;
    font-size: 28px;
    letter-spacing: 1px;
  }

  /* Back */
  .back-brand {
    position: absolute;
    top: 62px; left: 0; right: 0;
    display: flex; align-items: center; justify-content: center;
    gap: 18px;
  }
  .back-brand__dot {
    width: 34px; height: 34px;
    border-radius: 50%;
    background: var(--blue);
  }
  .back-brand__name {
    color: var(--blue);
    font-weight: 600;
    font-size: 30px;
    letter-spacing: 2px;
    text-transform: uppercase;
    line-height: 1;
  }
  .back-brand__sub {
    display: block;
    font-size: 13px;
    letter-spacing: 7px;
    margin-top: 6px;
  }
  .contact-person {
    position: absolute;
    left: 120px; top: 178px;
    text-align: right;
  }
  .contact-person__name {
    color: var(--blue);
    font-weight: 700;
    font-size: 24px;
  }
  .contact-person__title {
    color: var(--white);
    font-size: 15px;
  }
  .contact-list {
    position: absolute;
    left: 350px; top: 182px;
    list-style: none;
  }
  .contact-list li {
    display: flex; align-items: center; gap: 12px;
    color: var(--white);
    font-size: 16px;
    line-height: 27px;
  }
  .contact-list svg { width: 14px; height: 14px; flex: none; }
  .sound-strip {
    position: absolute;
    left: 0; right: 0; bottom: 0;
    height: 78px;
    background: linear-gradient(to top, #c9ccd0 0%, #9a9da2 55%, rgba(154,157,162,0) 100%);
  }
</style>
</head>
<body>

  <section class="card card--front" aria-label="Card front">
    <div class="front-mark">
      <span class="brand-name">Echoline</span>
    </div>
  </section>

  <section class="card card--back" aria-label="Card back">
    <div class="back-brand">
      <span class="back-brand__dot"></span>
      <span class="back-brand__name">Echoline<span class="back-brand__sub">Event Group</span></span>
    </div>

    <div class="contact-person">
      <p class="contact-person__name">Jane Porter</p>
      <p class="contact-person__title">Founder &amp; CEO</p>
    </div>

    <ul class="contact-list">
      <li>
        <svg viewBox="0 0 16 16" aria-hidden="true"><path fill="var(--blue)" d="M3.6 1.5l2.2 2.6-1.3 1.6c.9 2 2.3 3.5 4.3 4.4l1.6-1.3 2.6 2.2-1.3 2.5C6.4 13.3 2.7 9.6 1.1 4.3z"/></svg>
        555 0142 0187
      </li>
      <li>
        <svg viewBox="0 0 16 16" aria-hidden="true"><rect x="1" y="3" width="14" height="10" fill="var(--blue)"/><path d="M1.5 3.5L8 9l6.5-5.5" fill="none" stroke="var(--card)" stroke-width="1.3"/></svg>
        jane@echoline.com
      </li>
      <li>
        <svg viewBox="0 0 16 16" aria-hidden="true"><circle cx="8" cy="8" r="6.5" fill="none" stroke="var(--blue)" stroke-width="1.5"/><ellipse cx="8" cy="8" rx="2.8" ry="6.5" fill="none" stroke="var(--blue)" stroke-width="1.2"/><path d="M1.5 8h13" stroke="var(--blue)" stroke-width="1.2"/></svg>
        www.echoline.com
      </li>
    </ul>

    <div class="sound-strip" role="img" aria-label="Silver sound-wave equalizer bars along the bottom edge"></div>
  </section>

</body>
</html>
```